Clever & creative business card needed for a pediatric dentist.

We need a business card for a pediatric dentist that is building a brand-new pediatric dental practice. He is funny, outgoing, and sociable, and he hopes to give his business card to dentists and pediatricians so that he can give them information of where to refer infants, children, and teenagers that need high quality and attainable dental care.

The name of the dental practice is Copper Fern Pediatric Dentistry. Logo design .png / .pdf/ .jpg are provided to aid in the design.

The dentist's last name is Tolvan (which sounds like "burger", as in "hamburger” or “cheeseburger"). Since it is pediatric practice, kudos will be given to designs that implement a little joke into the design - but hopefully in a small or hidden way (such as putting something like a cheeseburger on the back of the card, or hiding it an an abstract way).

Thank you!

Please make a design that incorporates colors. It should be fun! Not too serious. It does not have to follow the color scheme of the logos.

```html
<!DOCTYPE html>
<html lang="en">
<head>
<meta charset="utf-8">
<title>Copper Fern Pediatric Dentistry – Business Card</title>
<link rel="stylesheet" href="https://fonts.googleapis.com/css2?family=Poppins:wght@300;400;500;600&display=swap">
<style>
  :root {
    --page-bg: #101010;
    --card-bg: #262626;
    --card-edge: #2e9e5b;
    --brand-green: #3fae68;
    --text-light: #f2f2f2;
    --text-muted: #c9c9c9;
    --rule: #5a5a5a;
    --emboss: #353535;
  }
  * { margin: 0; padding: 0; box-sizing: border-box; }
  html, body {
    width: 1200px; height: 820px; overflow: hidden;
    background: var(--page-bg);
    font-family: "Poppins", sans-serif;
  }
  .stage {
    width: 1200px; height: 820px;
    display: flex; align-items: center; justify-content: center; gap: 40px;
  }
  .card {
    position: relative;
    width: 540px; height: 310px;
    background: var(--card-bg);
    border-left: 3px solid var(--card-edge);
    border-bottom: 3px solid var(--card-edge);
    box-shadow: 0 18px 40px rgba(0,0,0,.6);
    overflow: hidden;
  }
  /* Front */
  .brand {
    position: absolute; top: 62px; right: 60px;
    display: flex; align-items: center; gap: 12px;
  }
  .brand-dot {
    width: 22px; height: 22px; border-radius: 50%;
    background: var(--brand-green);
  }
  .brand-name {
    color: var(--text-light); font-weight: 500; font-size: 21px; line-height: 1.2;
    letter-spacing: .3px;
  }
  .divider {
    position: absolute; left: 40px; right: 40px; top: 150px;
    height: 1px; background: var(--rule);
  }
  .person { position: absolute; left: 40px; top: 172px; }
  .person-name {
    color: var(--brand-green); font-weight: 600; font-size: 17px; letter-spacing: .3px;
  }
  .person-title { color: var(--text-light); font-size: 13px; font-weight: 400; }
  .person-rule { width: 150px; height: 1px; background: var(--rule); margin: 12px 0 10px; }
  .contact-list { list-style: none; }
  .contact-list li {
    display: flex; align-items: center; gap: 9px;
    color: var(--text-light); font-size: 12.5px; line-height: 20px;
  }
  .contact-list svg { width: 13px; height: 13px; flex: none; }
  .address {
    position: absolute; right: 40px; top: 180px; text-align: right;
    color: var(--text-light); font-size: 12.5px; line-height: 19px;
  }
  /* Back */
  .joke-word {
    position: absolute; left: 150px; top: 70px;
    color: var(--emboss); font-size: 38px; font-weight: 300; letter-spacing: 2px;
  }
  .back-brand {
    position: absolute; right: 36px; bottom: 90px;
    display: flex; align-items: center; gap: 12px;
  }
</style>
</head>
<body>
<main class="stage">
  <section class="card card-front" aria-label="Business card front">
    <div class="brand">
      <span class="brand-dot"></span>
      <span class="brand-name">Copper Fern<br>Pediatric Dentistry</span>
    </div>
    <div class="divider"></div>
    <div class="person">
      <p class="person-name">MARCUS DELANE</p>
      <p class="person-title">Managing Director</p>
      <div class="person-rule"></div>
      <ul class="contact-list">
        <li>
          <svg viewBox="0 0 24 24" fill="none" stroke="var(--brand-green)" stroke-width="2.4"><path d="M5 3h4l2 5-3 2a12 12 0 0 0 6 6l2-3 5 2v4a2 2 0 0 1-2 2A17 17 0 0 1 3 5a2 2 0 0 1 2-2z"/></svg>
          044-555 018 342
        </li>
        <li>
          <svg viewBox="0 0 24 24" fill="none" stroke="var(--brand-green)" stroke-width="2.4"><rect x="2" y="5" width="20" height="14"/><path d="M2 5l10 8 10-8"/></svg>
          hello@copperfernkids.com
        </li>
        <li>
          <svg viewBox="0 0 24 24" fill="none" stroke="var(--brand-green)" stroke-width="2.2"><circle cx="12" cy="12" r="10"/><path d="M2 12h20M12 2c3 3 3 17 0 20M12 2c-3 3-3 17 0 20"/></svg>
          www.copperfernkids.com
        </li>
      </ul>
    </div>
    <p class="address">421, Address line goes here<br>45452, Country Name</p>
  </section>

  <section class="card card-back" aria-label="Business card back">
    <p class="joke-word">HAMBURGER</p>
    <div class="back-brand">
      <span class="brand-dot"></span>
      <span class="brand-name">Copper Fern<br>Pediatric Dentistry</span>
    </div>
  </section>
</main>
</body>
</html>
```